Label Design Project for a natural hair care line

Velora(tm) Hair Care System is an organic approach to healthy hair care for chemical free and chemically processed hair. I am looking for product labels for the line (there are 10 products in the line). Would like the labels to be modern yet elegant that would look great if the labels were clear and on blue bottles.

Target Market(s)

Natural products enthusiasts

Industry/Entity Type

Hair

Requirements
Must have
• The product name and description
Nice to have
• A touch of graphics but not too busy, must be able to read on a blue bottle
Should not have
• Anything that gives the product too whimsical of look (too many swirling lines on letters)

```html
<!DOCTYPE html>
<html lang="en">
<head>
<meta charset="utf-8">
<title>Velora Hair Care System – Label Range</title>
<link rel="stylesheet" href="https://fonts.googleapis.com/css2?family=Lora:wght@500&family=Open+Sans:wght@400;600&display=swap">
<style>
  :root {
    --backdrop: #f1f1f2;
    --bottle-blue: #1b2ec4;
    --bottle-blue-light: #2f43d2;
    --lid-navy: #0b0f24;
    --label-line: #e8ecff;
    --ink-white: #ffffff;
    --accent-cyan: #5ccaf2;
    --art-fill-blue: #2f6fdc;
    --art-fill-navy: #1d4a7c;
  }
  * { box-sizing: border-box; margin: 0; padding: 0; }
  html, body { width: 1200px; height: 683px; overflow: hidden; background: var(--backdrop); }
  .range { position: relative; width: 1200px; height: 683px; font-family: "Open Sans", sans-serif; color: var(--ink-white); }

  .bottle-panel {
    position: absolute;
    background: linear-gradient(90deg, var(--bottle-blue) 0%, var(--bottle-blue-light) 45%, var(--bottle-blue) 100%);
    border-radius: 14px;
  }
  .bottle-panel.tall { width: 134px; height: 390px; top: 242px; }
  .bottle-panel.short { width: 108px; height: 300px; top: 332px; }

  .label { position: absolute; overflow: hidden; border: 1px solid var(--label-line); }
  .tall .label { left: 14px; top: 104px; width: 107px; height: 187px; }
  .short .label { left: 9px; top: 94px; width: 91px; height: 160px; }

  .brand { position: absolute; left: 0; right: 0; text-align: center; }
  .tall .brand { top: 14px; }
  .short .brand { top: 12px; }
  .brand-name { font-family: "Lora", serif; font-weight: 500; font-size: 20px; line-height: 1; }
  .short .brand-name { font-size: 17px; }
  .brand-name sup { font-family: "Open Sans", sans-serif; font-size: 4px; vertical-align: top; }
  .brand-rule { height: 1px; width: 74%; margin: 4px auto 3px; background: var(--ink-white); }
  .brand-line { font-size: 5px; letter-spacing: 1.5px; text-transform: uppercase; }
  .short .brand-line { font-size: 4.4px; letter-spacing: 1.2px; }

  .product-name { position: absolute; left: 7px; font-weight: 400; font-size: 10px; line-height: 1.1; color: var(--accent-cyan); white-space: nowrap; }
  .short .product-name { left: 7px; font-size: 9.5px; }
  .product-type { position: absolute; left: 7px; font-size: 5.6px; font-weight: 600; line-height: 1.3; z-index: 1; }
  .short .product-type { font-size: 5px; }
  .product-note { position: absolute; left: 7px; font-size: 3.6px; line-height: 1.3; width: 48px; z-index: 1; }
  .size { position: absolute; bottom: 6px; left: 0; right: 0; text-align: center; font-size: 3.8px; }

  .art-area { position: absolute; border-radius: 50%; background: var(--art-fill-blue); }
  .tall .art-area { left: 48px; top: 102px; width: 64px; height: 64px; }
  .short .art-area { left: 42px; top: 87px; width: 56px; height: 56px; }

  .lid-label { position: absolute; left: 896px; top: 121px; width: 296px; height: 296px; border-radius: 50%;
    background: var(--lid-navy); }
  .lid-inner { position: absolute; left: 10px; top: 10px; width: 276px; height: 276px; border-radius: 50%; border: 1.5px solid var(--ink-white); overflow: hidden; }
  .lid-inner .brand { top: 36px; }
  .lid-inner .brand-name { font-size: 35px; }
  .lid-inner .brand-name sup { font-size: 6px; }
  .lid-inner .brand-rule { width: 118px; margin: 7px auto 6px; }
  .lid-inner .brand-line { font-size: 7.5px; letter-spacing: 2.2px; }
  .lid-inner .product-name { left: 40px; top: 122px; font-size: 21px; }
  .lid-inner .product-type { left: 40px; top: 164px; font-size: 9.5px; line-height: 1.3; }
  .lid-inner .size { bottom: 12px; font-size: 6.5px; }
  .lid-inner .art-area { left: 126px; top: 97px; width: 152px; height: 152px; background: var(--art-fill-navy); }
</style>
</head>
<body>
<main class="range">

  <section class="bottle-panel tall" style="left:62px">
    <div class="label">
      <div class="brand"><div class="brand-name">Velora<sup>TM</sup></div><div class="brand-rule"></div><div class="brand-line">Hair Care System</div></div>
      <div class="art-area" role="img" aria-label="Decorative circle artwork area"></div>
      <h2 class="product-name" style="top:80px">Soft Whisper</h2>
      <p class="product-type" style="top:110px">Moisture<br>Detangling<br>Mist</p>
      <p class="size">8 fl. oz / 237 ml</p>
    </div>
  </section>

  <section class="bottle-panel tall" style="left:218px">
    <div class="label">
      <div class="brand"><div class="brand-name">Velora<sup>TM</sup></div><div class="brand-rule"></div><div class="brand-line">Hair Care System</div></div>
      <div class="art-area" role="img" aria-label="Decorative circle artwork area"></div>
      <h2 class="product-name" style="top:77px">Grand Encore</h2>
      <p class="product-type" style="top:106px">Conditioning<br>Silk Pressing<br>Oil</p>
      <p class="size">8 fl. oz / 237 ml</p>
    </div>
  </section>

  <section class="bottle-panel tall" style="left:374px">
    <div class="label">
      <div class="brand"><div class="brand-name">Velora<sup>TM</sup></div><div class="brand-rule"></div><div class="brand-line">Hair Care System</div></div>
      <div class="art-area" role="img" aria-label="Decorative circle artwork area"></div>
      <h2 class="product-name" style="top:77px">Brilliance</h2>
      <p class="product-type" style="top:102px">Stimulating<br>Mint<br>Shampoo</p>
      <p class="product-note" style="top:134px">Conditioning shampoo to cleanse, revitalize and moisturize hair with a blend of organic peppermint and sweet dark chocolate.</p>
      <p class="size">8 fl. oz / 237 ml</p>
    </div>
  </section>

  <section class="bottle-panel short" style="left:527px">
    <div class="label">
      <div class="brand"><div class="brand-name">Velora<sup>TM</sup></div><div class="brand-rule"></div><div class="brand-line">Hair Care System</div></div>
      <div class="art-area" role="img" aria-label="Decorative circle artwork area"></div>
      <h2 class="product-name" style="top:64px">Spotlight</h2>
      <p class="product-type" style="top:90px">Luminous<br>Shine<br>Spray</p>
      <p class="size">4 oz / 118 ml</p>
    </div>
  </section>

  <section class="bottle-panel short" style="left:657px">
    <div class="label">
      <div class="brand"><div class="brand-name">Velora<sup>TM</sup></div><div class="brand-rule"></div><div class="brand-line">Hair Care System</div></div>
      <div class="art-area" role="img" aria-label="Decorative circle artwork area"></div>
      <h2 class="product-name" style="top:64px">Candor</h2>
      <p class="product-type" style="top:90px">Heat<br>Protection<br>Spray</p>
      <p class="product-note" style="top:117px; width:38px">Heat protector with a lightweight feel for all hair types.</p>
      <p class="size">4 oz / 118 ml</p>
    </div>
  </section>

  <section class="bottle-panel short" style="left:786px">
    <div class="label">
      <div class="brand"><div class="brand-name">Velora<sup>TM</sup></div><div class="brand-rule"></div><div class="brand-line">Hair Care System</div></div>
      <div class="art-area" role="img" aria-label="Decorative circle artwork area"></div>
      <h2 class="product-name" style="top:64px">Radiance</h2>
      <p class="product-type" style="top:90px">Conditioning<br>Shine<br>Oil</p>
      <p class="size">4 oz / 118 ml</p>
    </div>
  </section>

  <section class="lid-label">
    <div class="lid-inner">
      <div class="art-area" role="img" aria-label="Decorative circle artwork area"></div>
      <div class="brand"><div class="brand-name">Velora<sup>TM</sup></div><div class="brand-rule"></div><div class="brand-line">Hair Care System</div></div>
      <h2 class="product-name">Cherish</h2>
      <p class="product-type">Edge<br>Control<br>Pomade</p>
      <p class="size">4 oz / 118 ml</p>
    </div>
  </section>

</main>
</body>
</html>
```